Brusque Premium Men's Shaving Cream Product Label . Cream packaged in a Amber Jar/Black Top Cap.

Please include information ( see Brusque design Template attachment) designed on a Round Top cap. Label Diameter: 3.125" NOTE: Design this First,
Wrap Around Label: 11.3125 x 0.875" (w x h): NOTE: Required latter after selection of Final Design Selection.
Shave Cream packaged in an 8oz Low Profile Amber Jar/Black Top Cap.
Thanks

Target Market(s)

Prime Target-Men Ages 20yrs-65yrs+ and Women 20yrs-65yrs+( they purchase ovr 55% of these Mens care products for partner/spouse/friend.

Industry/Entity Type

Personel Care/Cosmetics/NaturalHealthcare

Other font styles liked:
• At this stage if you would like to submi a desigh that would include both a Top Label and your Wrap-around label on a Amber jar/black top lid. It would be helpful to see how it would look complete. Thanks . Please refer to the updated design Graphic Template for copy and layout . Questions? Let me know. Thanks.Please now use TIMBERVALE on label designs. Thanks! Please see image attachment for added Tree Image Vector that can be added to your design instead of the Original Tree Image .

Requirements
Must have
• Look and Feel of a Quality/Premium Mens Skincare Brand with a Masculine feel but attractive to women as well ( not Macho!).Think Unisex with a Male slant.
Nice to have
• Premium/Quality/Natural Skincare & Bodycare Brand
Should not have
• Not Macho. No Cartoony or Barber Tools/Bearded Men Images. Too gimicky and over-hyped!

```html
<!DOCTYPE html>
<html lang="en">
<head>
<meta charset="utf-8">
<title>Brusque Timbervale Shaving Cream – Top Cap Label</title>
<link rel="stylesheet" href="https://fonts.googleapis.com/css2?family=Cinzel:wght@400;600;700&family=Josefin+Sans:wght@400;600&display=swap">
<style>
  :root {
    --backdrop: #c2b399;
    --label-base: #8a8373;
    --label-light: #938c7c;
    --label-dark: #7e7768;
    --ink: #ffffff;
    --shadow: #2e2a24;
  }
  html, body {
    margin: 0;
    padding: 0;
    width: 1200px;
    height: 1200px;
    overflow: hidden;
    background: var(--backdrop);
  }
  .cap-label {
    display: block;
    width: 1200px;
    height: 1200px;
  }
  .brand-name {
    font-family: "Josefin Sans", sans-serif;
    font-weight: 600;
    font-size: 36px;
    fill: var(--ink);
  }
  .product-name {
    font-family: "Cinzel", serif;
    font-weight: 700;
    font-size: 70px;
    fill: var(--ink);
  }
  .product-shadow { fill: var(--shadow); }
  .product-type {
    font-family: "Cinzel", serif;
    font-weight: 600;
    font-size: 34px;
    fill: var(--ink);
  }
  .product-type-fr {
    font-family: "Cinzel", serif;
    font-weight: 700;
    font-size: 28px;
    fill: var(--ink);
  }
  .scent-line {
    font-family: "Cinzel", serif;
    font-weight: 600;
    font-size: 20px;
    fill: var(--ink);
  }
  .year-line {
    font-family: "Cinzel", serif;
    font-size: 19px;
    fill: var(--ink);
  }
  .net-weight {
    font-family: "Cinzel", serif;
    font-size: 22px;
    fill: var(--ink);
  }
  .ring-line { fill: none; stroke: var(--ink); }
</style>
</head>
<body>
<svg class="cap-label" viewBox="0 0 1200 1200" xmlns="http://www.w3.org/2000/svg">
  <defs>
    <radialGradient id="label-fill" cx="50%" cy="45%" r="60%">
      <stop offset="0%" stop-color="var(--label-light)"/>
      <stop offset="70%" stop-color="var(--label-base)"/>
      <stop offset="100%" stop-color="var(--label-dark)"/>
    </radialGradient>
    <path id="weight-arc" d="M 466 879 A 310 310 0 0 0 766 879"/>
  </defs>

  <!-- label disc -->
  <circle class="label-disc" cx="616" cy="608" r="384" fill="url(#label-fill)"/>

  <!-- border rings -->
  <g class="border-rings">
    <circle class="ring-line" cx="616" cy="608" r="370" stroke-width="3"/>
    <circle class="ring-line" cx="616" cy="608" r="365" stroke-width="1.2"/>
    <circle class="ring-line" cx="616" cy="608" r="357" stroke-width="4.5" stroke-linecap="round" stroke-dasharray="0 8.2"/>
    <circle class="ring-line" cx="616" cy="608" r="349" stroke-width="1.2"/>
    <circle class="ring-line" cx="616" cy="608" r="344" stroke-width="3"/>
  </g>

  <!-- inner side arcs -->
  <g class="inner-arcs">
    <path class="ring-line" stroke-width="1.6" d="M 764 352 A 294 294 0 0 1 764 862"/>
    <path class="ring-line" stroke-width="1.6" d="M 468 352 A 294 294 0 0 0 468 862"/>
  </g>

  <!-- brand -->
  <text class="brand-name" x="616" y="372" text-anchor="middle" textLength="212" lengthAdjust="spacing">BRUSQUE</text>

  <!-- tree emblem area -->
  <rect class="tree-emblem" role="img" aria-label="White tree of life illustration with leafy crown and spreading roots"
        x="520" y="416" width="176" height="184" rx="88" fill="var(--ink)" opacity="0.85"/>

  <!-- product name -->
  <text class="product-name product-shadow" x="619" y="679" text-anchor="middle" textLength="516" lengthAdjust="spacingAndGlyphs">Timbervale</text>
  <text class="product-name" x="616" y="676" text-anchor="middle" textLength="516" lengthAdjust="spacingAndGlyphs">Timbervale</text>

  <text class="product-type" x="617" y="740" text-anchor="middle" textLength="326" lengthAdjust="spacingAndGlyphs">Shaving Cream</text>
  <text class="product-type-fr" x="616" y="772" text-anchor="middle" textLength="276" lengthAdjust="spacingAndGlyphs">Crème De Rasage</text>

  <!-- divider -->
  <line class="ring-line" x1="532" y1="800" x2="700" y2="800" stroke-width="1.4"/>

  <text class="scent-line" x="616" y="838" text-anchor="middle" textLength="224" lengthAdjust="spacingAndGlyphs">Wildwood Accord</text>
  <g class="year-line-group">
    <line class="ring-line" x1="554" y1="862" x2="584" y2="862" stroke-width="1.4"/>
    <text class="year-line" x="618" y="868" text-anchor="middle" textLength="58" lengthAdjust="spacingAndGlyphs">1935</text>
    <line class="ring-line" x1="652" y1="862" x2="674" y2="862" stroke-width="1.4"/>
  </g>

  <!-- net weight on arc -->
  <text class="net-weight"><textPath href="#weight-arc" startOffset="50%" text-anchor="middle">150g (5.3 oz)</textPath></text>
</svg>
</body>
</html>
```